Business cards for law firm with global theme

I'd like business cards with contact info for two offices. They should include the colors and font of the new logo design, which is a stylized globe with an "F" in it. The feel should be very modern and professional.

```html
<!DOCTYPE html>
<html lang="en">
<head>
<meta charset="utf-8">
<title>Veranto Law – Business Cards</title>
<link href="https://fonts.googleapis.com/css2?family=Lato:wght@400;700&display=swap" rel="stylesheet">
<style>
  :root {
    --navy: #173f6e;
    --sky: #27a8e0;
    --ink: #454545;
    --paper: #ffffff;
    --backdrop: #ebe7df;
  }
  * { box-sizing: border-box; margin: 0; padding: 0; }
  html, body { width: 1200px; height: 1200px; overflow: hidden; }
  body {
    background: var(--backdrop);
    font-family: "Lato", sans-serif;
    position: relative;
  }
  .card {
    position: absolute;
    left: 150px;
    width: 900px;
    height: 515px;
    overflow: hidden;
    box-shadow: 0 6px 18px rgba(0,0,0,0.18);
  }
  .card-front { top: 55px; background: var(--paper); }
  .card-back { top: 630px; background: var(--navy); }
  .card-wave { position: absolute; inset: 0; width: 900px; height: 515px; }

  .brand { position: absolute; text-align: center; }
  .brand-mark { display: block; margin: 0 auto; border-radius: 50%; }
  .brand-name {
    display: block;
    font-weight: 700;
    letter-spacing: 1px;
    white-space: nowrap;
    text-transform: uppercase;
  }
  .card-front .brand { left: 70px; width: 340px; top: 140px; }
  .card-front .brand-mark { width: 130px; height: 130px; background: var(--sky); }
  .card-front .brand-name { color: var(--navy); font-size: 48px; margin-top: 26px; }

  .card-back .brand { left: 200px; width: 500px; top: 118px; }
  .card-back .brand-mark { width: 156px; height: 156px; background: var(--sky); }
  .card-back .brand-name { color: var(--paper); font-size: 58px; margin-top: 26px; }

  .divider {
    position: absolute;
    left: 447px; top: 143px;
    width: 3px; height: 230px;
    background: var(--sky);
  }
  .contact { position: absolute; left: 495px; top: 138px; color: var(--ink); }
  .contact-name {
    font-size: 27px; font-weight: 700; color: var(--navy);
    letter-spacing: 0.3px; line-height: 1;
  }
  .contact-name .surname { color: var(--sky); }
  .contact-role { font-size: 20px; margin-top: 10px; }
  .contact-address { font-size: 20px; line-height: 31px; margin-top: 18px; }
  .contact-lines { list-style: none; margin-top: 16px; font-size: 20px; line-height: 31px; }
  .contact-lines li { display: flex; align-items: center; gap: 10px; }
  .contact-lines svg { width: 19px; height: 19px; flex: none; }
</style>
</head>
<body>

<section class="card card-front">
  <div class="brand">
    <span class="brand-mark"></span>
    <span class="brand-name">Veranto Law</span>
  </div>

  <div class="divider"></div>

  <div class="contact">
    <p class="contact-name">DANIEL <span class="surname">HARPER</span></p>
    <p class="contact-role">President</p>
    <p class="contact-address">1287 Linden Avenue, Brookhaven<br>NC 4, United States</p>
    <ul class="contact-lines">
      <li>
        <svg viewBox="0 0 20 20" aria-hidden="true"><path d="M4 2 L7 2 L8.5 6 L6.5 7.5 Q8 11.5 12.5 13.5 L14 11.5 L18 13 L18 16 Q18 18 16 18 Q3 17 2 4 Q2 2 4 2 Z" fill="var(--sky)"/><path d="M12 2.5 A6 6 0 0 1 17.5 8" stroke="var(--sky)" stroke-width="1.6" fill="none"/><path d="M11.5 5.5 A3 3 0 0 1 14.5 8.5" stroke="var(--sky)" stroke-width="1.6" fill="none"/></svg>
        <span>000-000-000-000</span>
      </li>
      <li>
        <svg viewBox="0 0 20 20" aria-hidden="true"><rect x="1" y="4" width="18" height="12" fill="var(--sky)"/><path d="M1 4 L10 11 L19 4" stroke="#fff" stroke-width="1.4" fill="none"/><path d="M1 16 L7.5 9.5 M19 16 L12.5 9.5" stroke="#fff" stroke-width="1.2"/></svg>
        <span>info@websitename.com</span>
      </li>
      <li>
        <svg viewBox="0 0 20 20" aria-hidden="true" fill="none" stroke="var(--sky)" stroke-width="1.4"><circle cx="10" cy="10" r="8.3"/><ellipse cx="10" cy="10" rx="3.6" ry="8.3"/><path d="M1.7 10 H18.3 M3 6 H17 M3 14 H17"/></svg>
        <span>www.websitename.com</span>
      </li>
    </ul>
  </div>

  <svg class="card-wave" viewBox="0 0 900 515" aria-hidden="true">
    <path d="M0,414 Q500,515 900,436 L900,515 L0,515 Z" fill="var(--navy)"/>
    <path d="M490,486 Q740,475 900,413 L900,441 Q720,480 490,486 Z" fill="var(--sky)"/>
    <path d="M490,486 Q720,481 900,443" stroke="var(--paper)" stroke-width="2.5" fill="none"/>
  </svg>
</section>

<section class="card card-back">
  <svg class="card-wave" viewBox="0 0 900 515" aria-hidden="true">
    <path d="M0,415 Q500,515 900,440 L900,515 L0,515 Z" fill="var(--paper)"/>
    <path d="M490,487 Q740,477 900,418 L900,443 Q720,482 490,487 Z" fill="var(--sky)"/>
    <path d="M490,487 Q720,483 900,446" stroke="var(--navy)" stroke-width="2.5" fill="none"/>
  </svg>
  <div class="brand">
    <span class="brand-mark"></span>
    <span class="brand-name">Veranto Law</span>
  </div>
</section>

</body>
</html>
```